Very Simple Web Redesign Project - Using Photoshop

Required is a very simple website home page redesign for the following site: http://www.kestrelslateworks.com.au/
I require this as a Photoshop design.
The basic look and feel of the site needs to remain.
Specifically the colours don't need to be changed.
The positioning of the site is currently correct for the target market.
The site does not need to be made super slick looking. Just upgraded to a new version.
The current text can all be used.
The only menus necessary are a horizontal menu at the top, and a simple horizontal text menu at the bottom of the page. Do NOT retain the vertical menu on the home page (having the items "Our Gallery", "Our Services", "Enquire Now").
Give the horizontal menu the following items:
Home | Slate Roof Repairs | Slate Reroofing | Slate Roof Benefits | Other Services | Photo Gallery | FAQ's | Free Quote | Contact Us
The picture of the house at the top RHS of the page needs to be reduced in size by approx 50% and moved to the top LHS of the page.
Please place the following text into the top of the page:
"Call Now: 0427 618 302"
Keep the four pictures on the home page layout. Some larger images attached.
Thanks,
Ned
Updates
Hi,
Thanks for all the designs.
I am working with my client to get which one they like the most.
Thanks,
Ned

```html
<!DOCTYPE html>
<html lang="en">
<head>
<meta charset="utf-8">
<title>Kestrel Slateworks – The Slate Roof Specialists</title>
<link rel="stylesheet" href="https://fonts.googleapis.com/css2?family=Tenor+Sans&family=Lato:ital,wght@0,400;0,700;1,700;1,900&display=swap">
<style>
  :root {
    --green-dark: #2f6b12;
    --green-mid: #4d8f22;
    --green-bar: #3c7d19;
    --green-light: #8fd16a;
    --green-line: #6cc04a;
    --page: #f3f3f3;
    --ink: #1d1d1d;
    --muted: #2a2a2a;
    --white: #ffffff;
    --field-border: #c9c9c9;
  }
  * { box-sizing: border-box; margin: 0; padding: 0; }
  html, body { width: 1055px; height: 1200px; overflow: hidden; background: var(--page); }
  body { font-family: "Tenor Sans", sans-serif; color: var(--ink); }
  .page { position: relative; width: 1055px; height: 1200px; overflow: hidden; background: var(--page); }

  /* top navigation */
  .main-nav {
    position: absolute; left: 0; top: 0; width: 1055px; height: 27px;
    background: linear-gradient(to bottom, var(--green-mid), var(--green-bar));
  }
  .main-nav ul { list-style: none; display: flex; position: absolute; left: 56px; top: 0; height: 27px; align-items: center; }
  .main-nav li { color: var(--white); font-size: 13px; padding: 0 12px; position: relative; line-height: 27px; }
  .main-nav li + li::before { content: ""; position: absolute; left: 0; top: 8px; height: 12px; border-left: 1px solid rgba(255,255,255,.7); }
  .main-nav li.current { background: var(--green-dark); font-size: 15px; font-weight: bold; padding: 0 14px; }

  /* header */
  .brand { position: absolute; left: 72px; top: 43px; display: flex; align-items: center; gap: 20px; }
  .brand-mark { width: 92px; height: 98px; background: var(--green-dark); }
  .brand-name { font-size: 44px; color: var(--green-dark); line-height: 1; }
  .brand-tagline { position: absolute; left: 297px; top: 113px; font-size: 16px; color: var(--ink); }
  .call-now { position: absolute; left: 745px; top: 60px; display: flex; align-items: center; gap: 14px; }
  .call-now .label { font-size: 22px; line-height: 1; }
  .call-now .number { font-family: "Lato", sans-serif; font-weight: 700; font-size: 34px; line-height: 1.1; letter-spacing: .5px; }

  .divider { position: absolute; left: 56px; width: 939px; height: 12px; }

  /* showcase */
  .showcase { position: absolute; top: 186px; left: 74px; display: flex; gap: 27px; }
  .showcase .shot { width: 204px; height: 369px; box-shadow: 0 1px 2px rgba(0,0,0,.25); }
  .shot-1 { background: linear-gradient(to bottom, #9fb48a, #6f6a78 40%, #d9d4c8 65%, #7fae4a); }
  .shot-2 { background: linear-gradient(135deg, #7e7a86, #56505f 50%, #4a4453); }
  .shot-3 { background: linear-gradient(to bottom, #8e8b86, #7b7871 45%, #8a5a44); }
  .shot-4 { background: linear-gradient(to bottom, #bcd0e0, #65666c 40%, #7c7c78 70%, #b8b6ad); }

  /* welcome copy */
  .welcome { position: absolute; left: 56px; top: 612px; width: 585px; }
  .welcome h1 { font-family: "Lato", sans-serif; font-style: italic; font-weight: 900; font-size: 28px; margin-bottom: 14px; }
  .welcome p { font-size: 12.5px; line-height: 17px; margin-bottom: 17px; color: var(--muted); }

  .quote-side { position: absolute; left: 707px; top: 621px; width: 262px; }
  .quote-side h2 { font-family: "Lato", sans-serif; font-style: italic; font-weight: 700; font-size: 17.5px; color: var(--green-dark); margin-bottom: 7px; }
  .quote-photo { width: 261px; height: 131px; border: 1px solid #c8c8c8; border-radius: 4px;
    background: linear-gradient(to right, #e9eef3, #c9d7e4 45%, #f0e4d6); margin-bottom: 16px; }
  .quote-side p { font-size: 12.5px; line-height: 17px; color: var(--muted); }

  /* footer contacts */
  .contact { position: absolute; left: 59px; top: 961px; width: 272px; }
  .footer-heading { font-size: 17px; color: var(--green-dark); margin-bottom: 14px; }
  .contact-item { font-family: "Lato", sans-serif; font-weight: 700; font-size: 12.5px; line-height: 16px; padding-bottom: 10px; margin-bottom: 10px; border-bottom: 1px dotted #b5b5b5; display: flex; gap: 6px; }
  .contact-item:last-child { border-bottom: none; }
  .contact-item svg { flex: none; margin-top: 2px; }

  .footer-brand { position: absolute; left: 430px; top: 966px; width: 196px; text-align: center; }
  .footer-brand .brand-mark { width: 90px; height: 96px; margin: 0 auto 10px; }
  .footer-brand .brand-name { font-size: 26px; }
  .footer-brand .brand-tag { font-size: 12.5px; margin-top: 6px; }

  .quick-form { position: absolute; left: 733px; top: 961px; width: 259px; }
  .quick-form .field { display: block; width: 259px; height: 24px; margin-bottom: 6px; background: var(--white); border: 1px solid var(--field-border);
    font-family: "Lato", sans-serif; font-size: 11px; color: #444; padding: 4px 10px; }
  .quick-form .field.message { height: 67px; }
  .form-actions { display: flex; gap: 17px; margin-left: 57px; margin-top: 6px; }
  .btn { width: 68px; height: 23px; border-radius: 4px; color: var(--white); font-family: "Lato", sans-serif; font-weight: 700; font-size: 12px;
    display: flex; align-items: center; justify-content: center; border: 1px solid #9a9a9a; letter-spacing: .5px; }
  .btn-submit { background: linear-gradient(to bottom, #4e9a24, #2c6b0f); }
  .btn-clear { background: linear-gradient(to bottom, #a8a8a8, #7a7a7a); }

  /* bottom bar */
  .site-footer { position: absolute; left: 0; top: 1162px; width: 1055px; height: 38px;
    background: linear-gradient(to bottom, var(--green-mid), var(--green-bar)); color: var(--white);
    font-family: "Lato", sans-serif; font-weight: 700; font-size: 11px; }
  .site-footer .copyright { position: absolute; left: 57px; top: 13px; }
  .footer-nav { position: absolute; right: 61px; top: 13px; list-style: none; display: flex; }
  .footer-nav li { padding: 0 8px; border-left: 1px solid rgba(255,255,255,.7); line-height: 12px; }
  .footer-nav li:first-child { border-left: none; }
  .footer-nav li:last-child { padding-right: 0; }
</style>
</head>
<body>
<div class="page">

  <nav class="main-nav">
    <ul>
      <li class="current">Home</li>
      <li>Slate Roof Repairs</li>
      <li>Slate Reroofing</li>
      <li>Slate Roof Benefits</li>
      <li>Other Services</li>
      <li>Photo Gallery</li>
      <li>FAQ's</li>
      <li>Free Quote</li>
      <li>Contact Us</li>
    </ul>
  </nav>

  <header>
    <div class="brand">
      <div class="brand-mark" role="img" aria-label="Small square brand mark"></div>
      <div class="brand-name">Kestrel Slateworks</div>
    </div>
    <div class="brand-tagline">The Slate Roof Specialists</div>

    <div class="call-now">
      <svg width="36" height="48" viewBox="0 0 36 48" aria-hidden="true">
        <rect x="6" y="3" width="24" height="42" rx="5" fill="#2b3d4f" transform="rotate(-18 18 24)"/>
        <rect x="10" y="9" width="16" height="26" rx="2" fill="#6fb3e0" transform="rotate(-18 18 24)"/>
      </svg>
      <div>
        <div class="label">Call Now</div>
        <div class="number">0427 618 302</div>
      </div>
    </div>
  </header>

  <svg class="divider" style="top:157px" viewBox="0 0 939 12" aria-hidden="true">
    <rect x="0" y="0" width="443" height="10" fill="var(--green-light)"/>
    <rect x="443" y="5" width="356" height="5" fill="var(--green-light)"/>
    <rect x="799" y="8" width="140" height="3" fill="var(--green-line)"/>
  </svg>

  <section class="showcase">
    <div class="shot shot-1" role="img" aria-label="Slate turret roof on a garden gazebo"></div>
    <div class="shot shot-2" role="img" aria-label="Slate roof with a dormer window"></div>
    <div class="shot shot-3" role="img" aria-label="Slate roof slope beside a balcony"></div>
    <div class="shot shot-4" role="img" aria-label="Slate roof on a period home"></div>
  </section>

  <svg class="divider" style="top:577px" viewBox="0 0 939 12" aria-hidden="true">
    <rect x="0" y="9" width="138" height="3" fill="var(--green-line)"/>
    <rect x="138" y="6" width="357" height="5" fill="var(--green-light)"/>
    <rect x="495" y="1" width="444" height="10" fill="var(--green-light)"/>
  </svg>

  <main class="welcome">
    <h1>Welcome to Our Site</h1>
    <p>At Kestrel Slateworks we specialize in the upkeep, maintenance, repair and replacement of all types of slate roof as well as wood shingles.&nbsp; We can track down the leak that just won't go away or give your house a complete re-roof. We can also provide all your guttering needs.</p>
    <p>Kestrel Slateworks is a small company and as such we do not have the overheads that larger companies do.&nbsp; Quality work and attention to detail are our trademark.</p>
    <p>All photos on this website consist of work which I have personally done.&nbsp; The above photos provide at a quick glance a reasonable cross section of the type of work I do.</p>
    <p>By clicking on the Photo Gallery link you can see other work including some before and after shots.</p>
    <p>Feel free to call at your earliest convenience to organise an obligation free quote or fill out a form by clicking on the Contact Us link below.</p>
  </main>

  <aside class="quote-side">
    <h2>Call now and arrange a free quote:</h2>
    <div class="quote-photo" role="img" aria-label="Friendly customer service team on headsets"></div>
    <p>We service all inner city suburbs of Sydney roughly covering an area encompassing Gordon to Epping, Mosman to Bondi, Coogee to Kogarah and Kingsgrove to Burwood and Concord.</p>
  </aside>

  <svg class="divider" style="top:929px" viewBox="0 0 939 12" aria-hidden="true">
    <rect x="0" y="0" width="443" height="10" fill="var(--green-light)"/>
    <rect x="443" y="5" width="356" height="5" fill="var(--green-light)"/>
    <rect x="799" y="8" width="140" height="3" fill="var(--green-line)"/>
  </svg>

  <section class="contact">
    <h3 class="footer-heading">Contact Us:</h3>
    <div class="contact-item">
      <svg width="18" height="11" viewBox="0 0 18 11" aria-hidden="true"><rect width="18" height="11" fill="#111"/><path d="M0 0 L9 6 L18 0" stroke="#fff" stroke-width="1.2" fill="none"/></svg>
      <div>Address:<br>14/208 Harlow St Redfern NSW<br>2016</div>
    </div>
    <div class="contact-item" style="padding-top:8px">
      <svg width="18" height="13" viewBox="0 0 18 13" aria-hidden="true"><path d="M1 4 Q9 -1 17 4 L15 6 L12 4 L6 4 L3 6 Z" fill="#111"/><rect x="3" y="6" width="12" height="7" rx="1" fill="#111"/></svg>
      <div>Tel:&nbsp; 0427 618 302<br>Fax:&nbsp; 02 93645527</div>
    </div>
    <div class="contact-item">
      <span style="font-size:13px">@</span>
      <div>Email: hugo@kestrelslateworks.com.au</div>
    </div>
  </section>

  <div class="footer-brand">
    <div class="brand-mark" role="img" aria-label="Small square brand mark"></div>
    <div class="brand-name">Kestrel Slateworks</div>
    <div class="brand-tag">The Slate Roof Specialists</div>
  </div>

  <section class="quick-form">
    <h3 class="footer-heading">Quick Contacts</h3>
    <div class="field">Name...</div>
    <div class="field">Email...</div>
    <div class="field message">Message...</div>
    <div class="form-actions">
      <div class="btn btn-submit">Submit</div>
      <div class="btn btn-clear">Clear</div>
    </div>
  </section>

  <footer class="site-footer">
    <div class="copyright">Copyright © 2011 Kestrel Slateworks&nbsp; | &nbsp;All Rights Reserved</div>
    <ul class="footer-nav">
      <li>Home</li>
      <li>About Us</li>
      <li>Contact Us</li>
    </ul>
  </footer>

</div>
</body>
</html>
```